Dentist logo, business card and website

I have done an amateur job of creating a logo, business card and website. I would like it to look more professional. the current website can be found at www.tobenkarsh.com - I would like the website to be built and run through wix.com. The content on the website is as I would like it but I am open to suggestions.

The logo should be simple, may be best to keep to the letter TK - maybe to look like the V is a reflection of the A? Again, I am open to suggestions (I have attached a couple of images I have used on presentations but I would like the logo that you design to have a 'no fill' background so it can be placed on slides (for presentations etc).

The colour scheme seems wrong for a dentist, perhaps duck egg with black writing would be better? This applies to the business card as well (I have attached a PDF of some I have had made in the past but again they look amateur and colour scheme is wrong. The business cards should be landscape, have the logo in the top right corner, my name and qualifications in the middle, and my website and physical address in the bottom left corner: Glenmorrow Dental Surgery, 41-43 Pellow Crescent, Cardiff CF22 9RW.

Target Market(s)

30-60 year olds

Industry/Entity Type

Dental

Contact Information for Business Card

Please see brief and uploads.

Logo Text

TK

Number of Pages Required

4 page

Font styles to use
Decorative
Script

Requirements
Must have
• A sophisticated mature feel.
Nice to have
• Simplicity.
Should not have
• Anything too complicated.

```html
<!DOCTYPE html>
<html lang="en">
<head>
<meta charset="utf-8">
<title>Toben Karsh – Restorative and Implant Dentist</title>
<link href="https://fonts.googleapis.com/css2?family=Montserrat:wght@500&family=Open+Sans:wght@400&family=Roboto:ital,wght@0,300;0,400;0,700;1,400&display=swap" rel="stylesheet">
<style>
  :root {
    --sky: #45c3f8;
    --ink: #2a2f33;
    --navy: #1d4a66;
    --dark: #232323;
    --paper: #f2f2f2;
    --muted: #8b8b8b;
    --white: #ffffff;
  }
  * { margin: 0; padding: 0; box-sizing: border-box; }
  html, body { width: 890px; height: 1200px; overflow: hidden; }
  body { position: relative; font-family: "Roboto", sans-serif; background: var(--white); color: var(--ink); }
  .abs { position: absolute; }
  .center { left: 0; width: 890px; text-align: center; }

  .site-header { top: 0; left: 0; width: 890px; height: 98px; background: var(--white); }
  .brand-dot { left: 424px; top: 13px; width: 42px; height: 42px; border: 3px solid var(--sky); border-radius: 50%; }
  .brand-name { top: 59px; font-family: "Montserrat", sans-serif; font-weight: 500; font-size: 13px; letter-spacing: 2px; color: var(--ink); }
  .brand-quals { top: 78px; font-family: "Montserrat", sans-serif; font-size: 7.5px; letter-spacing: 0.5px; color: var(--muted); }

  .main-nav { top: 98px; left: 0; width: 890px; height: 29px; background: var(--dark); }
  .main-nav a { position: absolute; top: 8px; font-size: 9px; color: var(--white); text-decoration: none; line-height: 14px; }
  .main-nav a.active { top: 7px; padding: 1px 7px; background: var(--sky); border-radius: 9px; }

  .hero { top: 127px; left: 0; width: 890px; height: 305px; background: linear-gradient(90deg, #e6eaec 0%, #f7f8f8 30%, #f4f6f7 70%, #e3e9ed 100%); }
  .hero-tooth { left: 710px; top: 30px; width: 150px; height: 220px; border-radius: 60px 60px 40px 40px; background: linear-gradient(180deg, #ffffff, #eef2f4); opacity: 0.8; }
  .hero-portrait { left: 122px; top: 31px; width: 220px; height: 220px; border-radius: 50%; background: radial-gradient(circle at 50% 40%, #d9b59c 0%, #c9a78e 35%, #3d5675 80%); }
  .hero-title { top: 82px; left: 330px; width: 470px; text-align: center; font-weight: 300; font-size: 28px; line-height: 33px; color: var(--ink); }
  .hero-title strong { font-weight: 700; color: var(--sky); }
  .hero-sub { top: 164px; left: 330px; width: 470px; text-align: center; font-family: "Open Sans", sans-serif; font-size: 17px; color: var(--navy); }
  .hero-practice { top: 194px; left: 330px; width: 470px; text-align: center; font-family: "Open Sans", sans-serif; font-size: 14px; letter-spacing: 0.3px; color: var(--navy); }

  .services { top: 434px; left: 0; width: 890px; height: 274px; background: var(--sky); }
  .service { top: 38px; width: 160px; text-align: center; }
  .service svg { display: block; margin: 0 auto; }
  .service span { display: block; margin-top: 7px; font-size: 10px; color: var(--white); }
  .services-cta { top: 131px; font-weight: 700; font-size: 20px; color: var(--white); }
  .btn-about { left: 377px; top: 194px; width: 136px; height: 32px; border: 1px solid var(--white); border-radius: 16px; color: var(--white); font-size: 13px; line-height: 30px; text-align: center; text-decoration: none; }

  .testimonials { top: 709px; left: 0; width: 890px; height: 301px; background: var(--paper); }
  .testimonials h2 { position: absolute; top: 39px; left: 0; width: 890px; text-align: center; font-weight: 300; font-size: 16px; color: var(--navy); }
  .avatar { left: 405px; top: 79px; width: 70px; height: 70px; border-radius: 50%; border: 3px solid var(--white); background: radial-gradient(circle at 50% 40%, #c99a80 0%, #8a6a4a 40%, #5f7a4a 65%, #d42a2a 90%); }
  .quote { top: 169px; left: 210px; width: 500px; text-align: center; font-style: italic; font-size: 8px; line-height: 13px; color: var(--muted); }
  .author { top: 215px; font-size: 11px; color: #111; }
  .author em { font-style: normal; font-size: 9px; color: var(--sky); }
  .dots { top: 244px; left: 417px; display: flex; gap: 4px; }
  .dots i { width: 8px; height: 8px; border-radius: 50%; background: #c4c4c4; }
  .dots i.on { background: var(--sky); }

  .site-footer { top: 1010px; left: 0; width: 890px; height: 190px; background: var(--dark); }
  .social { top: 34px; left: 398px; display: flex; align-items: center; gap: 7px; font-size: 9px; color: #a9a9a9; }
  .social i { width: 18px; height: 18px; border-radius: 50%; background: #3b5791; }
  .footer-nav a { position: absolute; top: 88px; font-size: 8.5px; color: #a9a9a9; text-decoration: none; }
  .footer-rule { top: 140px; left: 0; width: 890px; height: 1px; background: #333; }
  .copyright { top: 162px; font-size: 7px; color: #a9a9a9; }
</style>
</head>
<body>
  <header class="abs site-header">
    <div class="abs brand-dot"></div>
    <div class="abs center brand-name">TOBEN KARSH</div>
    <div class="abs center brand-quals">BDS (HONS) MJDF RCS (ENG)</div>
  </header>

  <nav class="abs main-nav">
    <a class="active" href="#" style="left:282px">Home</a>
    <a href="#" style="left:337px">About Me</a>
    <a href="#" style="left:399px">Testimonials</a>
    <a href="#" style="left:475px">Patient Resources</a>
    <a href="#" style="left:570px">Contact</a>
  </nav>

  <section class="abs hero">
    <div class="abs hero-tooth" role="img" aria-label="Soft background photo of a dental tooth model"></div>
    <div class="abs hero-portrait" role="img" aria-label="Portrait photo of the dentist in navy scrubs"></div>
    <h1 class="abs hero-title">I am a Restorative and Implant<br><strong>DENTIST</strong> Based in Cardiff</h1>
    <p class="abs hero-sub">I provide care for my patients at</p>
    <p class="abs hero-practice">GLENMORROW DENTAL SURGERY</p>
  </section>

  <section class="abs services">
    <div class="abs service" style="left:99px">
      <svg width="34" height="34" viewBox="0 0 34 34"><circle cx="17" cy="17" r="16" fill="none" stroke="#fff" stroke-width="1.5"/><path d="M9 12c0-3 3-4 5-3 1 .5 2 .5 3 0 2-1 5 0 5 3 0 3-1 5-1.5 8-.4 2-1.6 2-2 0l-.8-3c-.3-1-1.1-1-1.4 0l-.8 3c-.4 2-1.6 2-2 0C10 17 9 15 9 12z" fill="#fff"/><path d="M19 24l7-7" stroke="#fff" stroke-width="1.5"/></svg>
      <span>ANESTHESIA</span>
    </div>
    <div class="abs service" style="left:269px">
      <svg width="34" height="34" viewBox="0 0 34 34"><circle cx="17" cy="17" r="16" fill="none" stroke="#fff" stroke-width="1.5"/><path d="M10 11c0-3 3-4 5-3 1 .5 2 .5 3 0 2-1 5 0 5 3 0 3-1 5-1.5 8-.4 2-1.6 2-2 0l-.8-3c-.3-1-1.1-1-1.4 0l-.8 3c-.4 2-1.6 2-2 0C11 16 10 14 10 11z" fill="#fff"/><path d="M20 25l6-9" stroke="#fff" stroke-width="1.5"/></svg>
      <span>ORAL SURGERY</span>
    </div>
    <div class="abs service" style="left:447px">
      <svg width="34" height="34" viewBox="0 0 34 34"><circle cx="17" cy="17" r="16" fill="none" stroke="#fff" stroke-width="1.5"/><path d="M9 10c0-3 3-4 5-3 1 .5 2 .5 3 0 2-1 5 0 5 3 0 3-1 4-2 6H11c-1-2-2-3-2-6z" fill="#fff"/><path d="M15 17h4v8h-4z" fill="#fff"/></svg>
      <span>IMPLANTOLOGY</span>
    </div>
    <div class="abs service" style="left:620px">
      <svg width="34" height="34" viewBox="0 0 34 34"><circle cx="17" cy="17" r="16" fill="none" stroke="#fff" stroke-width="1.5"/><path d="M10 13c0-3 3-4 5-3 1 .5 2 .5 3 0 2-1 5 0 5 3 0 3-1 5-1.5 8-.4 2-1.6 2-2 0l-.8-3c-.3-1-1.1-1-1.4 0l-.8 3c-.4 2-1.6 2-2 0C11 18 10 16 10 13z" fill="#fff"/><path d="M17 9l3-4" stroke="#fff" stroke-width="1.5"/></svg>
      <span>ENDODONTICS</span>
    </div>
    <p class="abs center services-cta">Nervous? Let's see how can I help you.</p>
    <a class="abs btn-about" href="#">ABOUT ME</a>
  </section>

  <section class="abs testimonials">
    <h2>TESTIMONIALS</h2>
    <div class="abs avatar" role="img" aria-label="Photo of a smiling patient in a red scarf"></div>
    <p class="abs quote">“Lorem ipsum dolor sit amet, consectetur adipiscing elit. Duis risus nunc, porta quis eros eu, dignissim tempus lorem. Morbi vel pellentesque diam. Duis pellentesque mi sit amet mi tincidunt, vel facilisis nisl mattis. ”</p>
    <p class="abs center author">Maren Holt, <em>Place here</em></p>
    <div class="abs dots"><i></i><i></i><i class="on"></i><i></i><i></i></div>
  </section>

  <footer class="abs site-footer">
    <div class="abs social"><i></i>Chatterly</div>
    <nav class="footer-nav">
      <a href="#" style="left:279px">Home</a>
      <a href="#" style="left:330px">About Me</a>
      <a href="#" style="left:394px">Testimonials</a>
      <a href="#" style="left:472px">Patient Resources</a>
      <a href="#" style="left:569px">Contact</a>
    </nav>
    <div class="abs footer-rule"></div>
    <p class="abs center copyright">Copyright 2016 www.tobenkarsh.com All Right Reserved.</p>
  </footer>
</body>
</html>
```